Label for Skincare Brand

"Fernbrook Organics" - organic skincare brand
I need a label designed for my organic skincare brand. I have attached pics of brands I like, to give you an idea of style. I would like something minimal although some colour might work. Colours I like are pale blush pink and aqua. I would like a clean, minimalistic modern yet elegant label. Please look at the samples because they demonstrate the style I look for in a label. It is okay to add a graphical element into the design as long as it enhances or add value to the design.
We do not have a logo yet, so I'd appreciate if you could create a simple type logo for Fernbrook Organics similar to the examples attached.
Please can you do two different sizes: one cream jar and one serum bottle. Both will contain the same information.
___________________________________________________
1. Cream Jar (label size 42 x 190 mm) (clear glass with aluminium lid)
2. Serum Bottle (label size 50 x 110 mm) (clear glass with black pump)
FRONT SIDE:
Fernbrook Organics
Moonpetal
Ultimate Anti-Aging Cream
For Dry & Mature Skin
Organic & Palm Oil-Free
100 ml.
BACK SIDE:
Moonpetal Radiance Renewal Cream
An effective Day Cream that harnesses the best of science to target the signs of aging. The main active ingredient is K7M, a patented noncomedogenic lipid complex, carefully engineered from botanically-sourced lipids. It is composed of a variety of lipid types which are carefully combined in the same ratio as those found on healthy young skin of an average 22 year old.
Directions:
Apply to clean skin morning and night.
Ingredients:
Aloe Vera Leaf Juice, Cocos Nucifera Oil, Butyrospermum Parkii Butter, Jojoba Oil/Macadamia Seed Oil Esters (and) Squalene (and) Phytosteryl Macadamiate (and) Phytosterols, Potassium Olivoyl Hydrolyzed Oat Protein (and) Cetearyl Alcohol (and) Glyceryl Oleate (and) Glyceryl Stearat, Benzyl Alcohol, Dehydroacetic Acid.
Fernbrook Organics
3/6 Kellerton Parade West, Wahroonga, NSW 2076
www.fernbrookorganics.example
Any questions, please just ask away. Thank you.

```html
<!DOCTYPE html>
<html lang="en">
<head>
<meta charset="utf-8">
<title>Fernbrook Organics – Moonpetal Front Label</title>
<link rel="stylesheet" href="https://fonts.googleapis.com/css2?family=Montserrat:wght@400;500&display=swap">
<style>
  :root {
    --backdrop: #ececec;
    --label-white: #ffffff;
    --ink: #2b2b2b;
    --ink-soft: #555a59;
    --aqua-band: #d3e6e0;
    --aqua-ink: #6f9790;
    --aqua-deep: #3f5f59;
  }

  * { margin: 0; padding: 0; box-sizing: border-box; }

  html, body {
    width: 900px;
    height: 1200px;
    overflow: hidden;
    background: var(--backdrop);
    font-family: "Montserrat", sans-serif;
    color: var(--ink);
  }

  .canvas {
    position: relative;
    width: 900px;
    height: 1200px;
  }

  .label {
    position: absolute;
    left: 150px;
    top: 110px;
    width: 600px;
    height: 980px;
    background: var(--label-white);
    box-shadow: 0 2px 14px rgba(0, 0, 0, 0.06);
  }

  .brand-name {
    position: absolute;
    top: 282px;
    left: 0;
    width: 100%;
    text-align: center;
    font-size: 27px;
    font-weight: 400;
    letter-spacing: 0.03em;
    line-height: 1;
    color: var(--ink);
  }

  .product-name {
    position: absolute;
    left: 262px;
    bottom: 272px;
    writing-mode: vertical-rl;
    transform: rotate(180deg);
    font-size: 36px;
    font-weight: 400;
    letter-spacing: 0.1em;
    line-height: 1;
    color: var(--ink);
  }

  .claims-band {
    position: absolute;
    left: 0;
    top: 758px;
    width: 100%;
    height: 124px;
    background: var(--aqua-band);
    padding: 10px 0 0 58px;
    font-size: 21px;
    line-height: 26px;
    text-transform: uppercase;
    letter-spacing: 0.01em;
  }

  .claims-band .range { color: var(--aqua-ink); font-weight: 400; }
  .claims-band .product-type { color: var(--aqua-deep); font-weight: 500; }
  .claims-band .skin-type,
  .claims-band .formula-note { color: var(--aqua-ink); font-weight: 400; }

  .net-volume {
    position: absolute;
    left: 0;
    top: 908px;
    width: 100%;
    text-align: center;
    font-size: 22px;
    font-weight: 400;
    letter-spacing: 0.04em;
    color: var(--ink-soft);
  }
</style>
</head>
<body>
  <main class="canvas">
    <section class="label" aria-label="Moonpetal cream front label">
      <p class="brand-name">Fernbrook Organics</p>

      <h1 class="product-name">MOONPETAL</h1>

      <div class="claims-band">
        <p class="range">Ultimate</p>
        <p class="product-type">Anti-Aging Cream</p>
        <p class="skin-type">For Dry &amp; Mature Skin</p>
        <p class="formula-note">Organic &amp; Palm Oil-Free</p>
      </div>

      <p class="net-volume">100 ML.</p>
    </section>
  </main>
</body>
</html>
```